Blue Mesa Fuels-Ethanol Plant-Business Card Design

We are looking to incorporate a new logo on a new business card design. Can be vertical or horizontal.
We currently produce a variety of feed products as well as pharmaceutical grade ethanol that can be used in hand sanitizers, medications, and vaccines and hospitals for sterilization. We are also the first company to incorporate Carbon Capture and Storage (CCS) which takes all of our CO2 emissions and injects it deep into the earth-about 6400 feet below our facility.
For our logo we are looking for something professional, detailed, yet simple looking that can be used for all areas of our company. Something 'timeless' that can be used for many years to come, no matter what future projects our company takes on.
Industry/Entity Type
Corn/Ethanol Plant
Contact Information for Business Card
First & Last Name, Title, E-Mail, Office Phone: 555.218.4470 Ext. 1000 , Fax: 555.218.4471, Cell: 555.390.2816, Email: Info@bluemesafuels.example, Address: 5147 Hwy 3 N PO Box 29 Alder Flats 58497, Website: www.bluemesafuels.example
Look and feel

```html
<!DOCTYPE html>
<html lang="en">
<head>
<meta charset="utf-8">
<title>Blue Mesa Fuels – Business Card</title>
<link rel="stylesheet" href="https://fonts.googleapis.com/css2?family=Montserrat:wght@600;700;800&family=Open+Sans:wght@400;600&display=swap">
<style>
  :root {
    --canvas: #dcd9d6;
    --card: #ffffff;
    --ink: #2b2d38;
    --ink-soft: #4a4c55;
    --accent: #e0262a;
  }
  * { margin: 0; padding: 0; box-sizing: border-box; }
  html, body { width: 1200px; height: 1200px; overflow: hidden; }
  body {
    background: var(--canvas);
    font-family: "Open Sans", Arial, sans-serif;
    color: var(--ink);
    position: relative;
  }
  .card {
    position: absolute;
    left: 150px;
    width: 900px;
    height: 514px;
    background: var(--card);
    box-shadow: 0 6px 18px rgba(0,0,0,0.12);
  }
  .card--contact { top: 58px; }
  .card--brand { top: 628px; }

  .brand-name {
    display: flex;
    align-items: center;
    gap: 14px;
    font-family: "Montserrat", Arial, sans-serif;
    font-weight: 800;
    color: var(--ink);
    text-transform: uppercase;
    letter-spacing: 1px;
  }
  .brand-name__mark {
    background: var(--accent);
    flex: none;
  }

  .card--contact .brand-name { position: absolute; left: 90px; top: 88px; font-size: 26px; }
  .card--contact .brand-name__mark { width: 22px; height: 22px; }

  .person { position: absolute; left: 90px; top: 212px; }
  .person__name {
    font-family: "Montserrat", Arial, sans-serif;
    font-weight: 700;
    font-size: 30px;
    letter-spacing: 1px;
    color: var(--ink);
  }
  .person__title { font-size: 19px; color: var(--ink-soft); margin-top: 2px; }

  .divider {
    position: absolute;
    left: 90px;
    top: 316px;
    width: 730px;
    height: 2px;
    background: var(--accent);
  }

  .contact-col {
    position: absolute;
    top: 340px;
    list-style: none;
    font-size: 17px;
    color: var(--ink-soft);
  }
  .contact-col li { display: flex; align-items: center; gap: 10px; height: 32px; white-space: nowrap; }
  .contact-col svg { width: 16px; height: 16px; flex: none; fill: none; stroke: var(--ink); stroke-width: 2; }
  .contact-col--phones { left: 90px; }
  .contact-col--web { left: 340px; }
  .contact-col--address { left: 630px; line-height: 1.45; }
  .contact-col--address li { height: auto; align-items: flex-start; }
  .contact-col--address svg { margin-top: 4px; }

  .card--brand .brand-name {
    position: absolute;
    left: 0; right: 0; top: 0; bottom: 0;
    justify-content: center;
    font-size: 44px;
  }
  .card--brand .brand-name__mark { width: 36px; height: 36px; }
</style>
</head>
<body>

<section class="card card--contact" aria-label="Business card, contact side">
  <div class="brand-name"><span class="brand-name__mark"></span>Blue Mesa Fuels</div>

  <div class="person">
    <p class="person__name">JACK SMITH</p>
    <p class="person__title">Designation</p>
  </div>

  <div class="divider"></div>

  <ul class="contact-col contact-col--phones">
    <li>
      <svg viewBox="0 0 16 16"><path d="M3 1.5l3 3-1.6 1.8a9 9 0 0 0 5.3 5.3L11.5 10l3 3-1.8 2C7 15 1 9 1 3.3z" fill="#2b2d38" stroke="none"/></svg>
      555-218-4470
    </li>
    <li>
      <svg viewBox="0 0 16 16"><rect x="4" y="1.5" width="8" height="13" rx="1.5"/><line x1="7" y1="12" x2="9" y2="12"/></svg>
      555-218-4470
    </li>
  </ul>

  <ul class="contact-col contact-col--web">
    <li>
      <svg viewBox="0 0 16 16"><rect x="1.5" y="3.5" width="13" height="9"/><path d="M1.5 3.5l6.5 5 6.5-5"/></svg>
      info@bluemesafuels.example
    </li>
    <li>
      <svg viewBox="0 0 16 16"><circle cx="8" cy="8" r="6.5"/><path d="M1.5 8h13M8 1.5c-3 3.5-3 9.5 0 13M8 1.5c3 3.5 3 9.5 0 13"/></svg>
      www.bluemesafuels.example
    </li>
  </ul>

  <ul class="contact-col contact-col--address">
    <li>
      <svg viewBox="0 0 16 16"><path d="M8 15s-5-5.5-5-9a5 5 0 0 1 10 0c0 3.5-5 9-5 9z" fill="#2b2d38" stroke="none"/><circle cx="8" cy="6" r="1.8" fill="#fff" stroke="none"/></svg>
      <span>PO Box 29, 5147 Hwy 3 N<br>Alder Flats 58497</span>
    </li>
  </ul>
</section>

<section class="card card--brand" aria-label="Business card, brand side">
  <div class="brand-name"><span class="brand-name__mark"></span>Blue Mesa Fuels</div>
</section>

</body>
</html>
```